Design revision of an existing Executive Summary

Our company velnova is specialized in the field of performance engineering (load and performance testing as well as application performance monitoring). We are looking for a designer who could graphically "spice up" our current executive summary about our company velnova (www.velnova-ops.com). Maybe it would be possible to incorporate a pic of our website (e.g. https://www.velnova-ops.com/en/services/performance/) into this newly designed executive summary.

Attached you will find the current executive summary which should not change textually. It should just look fresher and more modern. Ideally, a visually appealing first / title page would precede the text.

```html
<!DOCTYPE html>
<html lang="en">
<head>
<meta charset="utf-8">
<title>velnova – Executive Summary</title>
<link href="https://fonts.googleapis.com/css2?family=Montserrat:wght@300;400&family=Roboto:wght@400;500;700&display=swap" rel="stylesheet">
<style>
  :root{
    --backdrop:#d6d8d7;
    --paper:#ffffff;
    --navy:#133f72;
    --navy-band:#1a4176;
    --sky:#5ab4da;
    --night:#0b1a33;
    --ink:#1c3f73;
    --white:#ffffff;
  }
  *{box-sizing:border-box;margin:0;padding:0}
  html,body{width:1200px;height:840px;overflow:hidden;background:var(--backdrop)}
  body{position:relative;font-family:"Roboto",Arial,sans-serif;color:var(--white)}
  .page{position:absolute;top:34px;width:541px;height:772px;overflow:hidden;background:var(--paper)}
  .page--cover{left:43px}
  .page--summary{left:616px}
  .page__shapes{position:absolute;inset:0;width:100%;height:100%}

  .cover-photo{position:absolute;left:0;top:0;width:541px;height:772px;
    clip-path:polygon(0 178px,218px 141px,541px 182px,541px 772px,0 772px);
    background:linear-gradient(180deg,#152d57 0%,#0f2143 45%,#0a1730 75%,#171a3a 100%)}
  .cover-logo{position:absolute;left:0;right:0;top:270px;text-align:center;
    font-family:"Montserrat",sans-serif;font-weight:300;font-size:62px;letter-spacing:1px;color:var(--white)}

  .contact{position:absolute;left:0;right:0;top:740px;display:flex;justify-content:center;gap:9px;
    font-size:8.6px;color:var(--white);white-space:nowrap}
  .contact__item{display:flex;align-items:center;gap:3px}
  .contact__icon{width:7px;height:7px;fill:var(--sky)}

  .brand{position:absolute;left:0;right:0;top:48px;text-align:center;
    font-family:"Montserrat",sans-serif;font-weight:400;font-size:38px;color:var(--ink);letter-spacing:1px}
  .tagline{position:absolute;left:0;right:0;top:88px;text-align:center;
    font-family:"Montserrat",sans-serif;font-size:13px;color:var(--ink)}

  .section{position:absolute;width:214px}
  .section__title{font-weight:700;font-size:16px;letter-spacing:.3px;line-height:1}
  .section__rule{width:64px;height:2px;background:var(--sky);margin-top:12px}
  .section p{font-size:8.9px;line-height:12.7px}
  .who{left:33px;top:186px}
  .who p{margin-top:18px}
  .team{left:33px;top:437px}
  .team p{margin-top:14px}
  .services{left:297px;top:186px;width:206px}

  .service{position:absolute;left:297px;width:210px}
  .service__head{display:flex;align-items:center;gap:8px}
  .service__name{font-weight:500;font-size:11.4px;color:var(--sky)}
  .service__icon{width:38px;height:38px;stroke:var(--sky);fill:none;stroke-width:1.4}
  .service p{font-size:8.9px;line-height:12.7px}
  .service--load{top:212px}
  .service--load p{margin-top:12px}
  .service--apm{top:362px}
  .service--apm p{margin-top:14px}
  .service--train{top:503px}
  .service--train p{margin-top:14px}

  .customers-title{position:absolute;left:0;right:0;top:654px;text-align:center;font-weight:700;font-size:15px;letter-spacing:.4px}
  .customers{position:absolute;left:0;top:668px;width:541px;height:54px;background:var(--paper);
    display:flex;align-items:center;justify-content:space-around;padding:0 20px;font-weight:700;font-size:12px}
  .customer{display:flex;align-items:center;gap:4px}
  .customer__mark{width:10px;height:10px}
  .c-red{color:#d52b1e}.c-blue{color:#1a6fb5}.c-navy{color:#1d3f7a}.c-green{color:#1b8a4a}
</style>
</head>
<body>

<section class="page page--cover">
  <svg class="page__shapes" viewBox="0 0 1035 1476" preserveAspectRatio="none" aria-hidden="true">
    <polygon points="0,224 418,270 0,341" fill="var(--navy-band)"/>
    <polygon points="418,270 1035,172 1035,348" fill="var(--sky)"/>
  </svg>
  <div class="cover-photo" role="img" aria-label="Dusk city skyline with light trails of traffic on a highway, tinted in deep blue"></div>
  <div class="cover-logo">velnova</div>
  <footer class="contact">
    <span class="contact__item"><svg class="contact__icon" viewBox="0 0 10 10"><path d="M2 0h2l1 3-1.5 1a6 6 0 0 0 2.5 2.5L7 5l3 1v2c0 1-1 2-2 2A8 8 0 0 1 0 2C0 1 1 0 2 0z"/></svg>+43 - 1 - 48 12 90 3300</span>
    <span class="contact__item"><svg class="contact__icon" viewBox="0 0 10 8"><path d="M0 0h10v8H0z"/></svg>office@velnova-ops.com</span>
    <span class="contact__item"><svg class="contact__icon" viewBox="0 0 10 10"><circle cx="5" cy="5" r="5"/></svg>www.velnova-ops.com</span>
    <span class="contact__item"><svg class="contact__icon" viewBox="0 0 10 10"><rect width="10" height="10"/></svg>www.proflink.net/company/velnova</span>
  </footer>
</section>

<section class="page page--summary">
  <svg class="page__shapes" viewBox="0 0 1035 1476" preserveAspectRatio="none" aria-hidden="true">
    <polygon points="0,341 418,270 1035,348 1035,1476 0,1476" fill="var(--navy)"/>
    <polygon points="0,224 418,270 0,341" fill="var(--navy-band)"/>
    <polygon points="418,270 1035,172 1035,348" fill="var(--sky)"/>
  </svg>
  <div class="brand">velnova</div>
  <div class="tagline">Performance matters.</div>

  <div class="section who">
    <h2 class="section__title">WHO WE ARE?</h2>
    <div class="section__rule"></div>
    <p>Velnova is the go-to-company in the very specialized area of performance engineering. Whether microservices in the cloud or legacy on-premise: We will show you the added value of load &amp; performance tests, performance tuning or monitoring solutions.</p>
    <p style="margin-top:12.7px">In the area of application performance monitoring, we like to work with the enterprise solution from industry leader Tracewell. velnova is Tracewell Premier Partner and therefore amongst an exclusive group of companies in the EMEA region specialized in Tracewell.</p>
  </div>

  <div class="section team">
    <h2 class="section__title">ABOUT OUR TEAM</h2>
    <div class="section__rule"></div>
    <p>Our performance engineers guide our customers through the whole process of performance testing by providing best practices for test design and test strategies, setting up infrastructure, carrying out performance tests as well as preparing the reporting. If required, our performance engineers go beyond reporting by identifying the actual bottlenecks and even performing code reviews. As we offer to play such an active role in fixing performance defects, all our consultants are well-skilled software engineers.</p>
  </div>

  <div class="section services">
    <h2 class="section__title">OUR SERVICES</h2>
    <div class="section__rule"></div>
  </div>

  <div class="service service--load">
    <div class="service__head"><span class="service__name">Load &amp; Performance Testing</span>
      <svg class="service__icon" viewBox="0 0 40 40"><circle cx="20" cy="17" r="8"/><line x1="14" y1="23" x2="5" y2="33"/><path d="M12 10a9 9 0 0 1 17-2 6 6 0 0 1 4 11"/></svg></div>
    <p>An often-neglected necessity to ensure the speed, stability and reliability of your IT applications and digital services. If you expect many users rushing in on your digital roads, performance tests are required to provide the best experience for your customers.</p>
  </div>

  <div class="service service--apm">
    <div class="service__head"><span class="service__name">APM &amp; Observability</span>
      <svg class="service__icon" viewBox="0 0 40 40"><circle cx="22" cy="16" r="11"/><line x1="14" y1="24" x2="4" y2="34"/><line x1="18" y1="21" x2="18" y2="15"/><line x1="22" y1="21" x2="22" y2="11"/><line x1="26" y1="21" x2="26" y2="13"/></svg></div>
    <p>Follow the experience of users and pinpoint the root-cause of problems as fast as possible in case of an undesired event and get business insights like usage statistics and conversion rates just along the way.</p>
  </div>

  <div class="service service--train">
    <div class="service__head"><span class="service__name">Trainings &amp; Workshops</span>
      <svg class="service__icon" viewBox="0 0 40 40"><rect x="18" y="4" width="16" height="26"/><line x1="22" y1="10" x2="30" y2="10"/><line x1="22" y1="15" x2="30" y2="15"/><line x1="22" y1="20" x2="30" y2="20"/><circle cx="10" cy="14" r="4"/><line x1="8" y1="20" x2="6" y2="36"/><line x1="12" y1="20" x2="14" y2="36"/></svg></div>
    <p>Enable your own performance testing team by learning innovative approaches such as the automation of quality gates and automate performance feedback or get started with the basic methodology training.</p>
  </div>

  <h2 class="customers-title">VALUED CUSTOMERS</h2>
  <div class="customers">
    <span class="customer c-red">Norvik IT</span>
    <span class="customer c-red">Baumfeld</span>
    <span class="customer c-blue"><svg class="customer__mark" viewBox="0 0 10 10"><rect width="10" height="10" fill="#1aa3d9"/></svg>Stadt IT</span>
    <span class="customer c-navy">Alvera</span>
    <span class="customer c-red">Kammer IH</span>
    <span class="customer c-green"><svg class="customer__mark" viewBox="0 0 10 10"><rect width="10" height="10" fill="#1b8a4a"/></svg>Gemeindenet</span>
  </div>

  <footer class="contact">
    <span class="contact__item"><svg class="contact__icon" viewBox="0 0 10 10"><path d="M2 0h2l1 3-1.5 1a6 6 0 0 0 2.5 2.5L7 5l3 1v2c0 1-1 2-2 2A8 8 0 0 1 0 2C0 1 1 0 2 0z"/></svg>+43 - 1 - 48 12 90 3300</span>
    <span class="contact__item"><svg class="contact__icon" viewBox="0 0 10 8"><path d="M0 0h10v8H0z"/></svg>office@velnova-ops.com</span>
    <span class="contact__item"><svg class="contact__icon" viewBox="0 0 10 10"><circle cx="5" cy="5" r="5"/></svg>www.velnova-ops.com</span>
    <span class="contact__item"><svg class="contact__icon" viewBox="0 0 10 10"><rect width="10" height="10"/></svg>www.proflink.net/company/velnova</span>
  </footer>
</section>

</body>
</html>
```